Finance Product Agency Business Card Design

We're an agency that provides products (service contracts, gap insurance, tire and wheel, etc) and support to dealership finance departments. We specialize in training finance producers to maximize their potential and also keep them up to date on the ever changing compliance and legal landscape. I'll attach an image of our logo, excited to see what you all come up with. Would also be interested in discussing our new website design with the winner.

Target Market(s)

auto dealerships

Industry/Entity Type

Business

Contact Information for Business Card

Dale Hoskirk
Phone 517.364.2908
Fax 877.245.3196
email Dale.Hoskirk@brightlanecoverage.com

Requirements
Must have
• basic contact information
Nice to have
• looking for something professional but modern

```html
<!DOCTYPE html>
<html lang="en">
<head>
<meta charset="utf-8">
<title>Brightlane Coverage – Business Card</title>
<link rel="stylesheet" href="https://fonts.googleapis.com/css2?family=Lato:wght@400;700;900&display=swap">
<style>
  :root {
    --teal: #2a6475;
    --teal-dark: #1f4f5d;
    --charcoal: #262626;
    --paper: #ffffff;
    --paper-warm: #f6f5f3;
    --rule: #5a5a5a;
    --text-light: #e6e6e6;
    --backdrop: #e9e8e5;
  }
  * { box-sizing: border-box; margin: 0; padding: 0; }
  html, body {
    width: 1200px; height: 799px; overflow: hidden;
    background: var(--backdrop);
    font-family: "Lato", Arial, sans-serif;
  }
  .stage {
    position: relative; width: 1200px; height: 799px;
    display: flex; align-items: center; justify-content: center; gap: 60px;
  }
  .card {
    position: relative; width: 520px; height: 297px; overflow: hidden;
    box-shadow: 0 6px 18px rgba(0,0,0,.18);
  }
  .card svg.card-shapes { position: absolute; inset: 0; }

  /* Brand name lockup */
  .brand { position: absolute; display: flex; align-items: center; }
  .brand-dot { border-radius: 50%; background: var(--teal); flex: none; }
  .brand-name {
    font-weight: 900; color: var(--teal-dark);
    letter-spacing: .02em; line-height: 1; white-space: nowrap;
  }

  /* Front */
  .card-front { background: var(--paper); }
  .card-front .brand { left: 0; right: 0; top: 96px; justify-content: center; gap: 16px; }
  .card-front .brand-dot { width: 48px; height: 48px; }
  .card-front .brand-name { font-size: 34px; }

  /* Back: lockup stacked on two lines so it stays inside the light panel */
  .card-back { background: var(--paper-warm); }
  .card-back .brand { left: 24px; top: 106px; width: 196px; gap: 12px; }
  .card-back .brand-dot { width: 34px; height: 34px; }
  .card-back .brand-name { font-size: 21px; line-height: 1.1; }

  .holder-name {
    position: absolute; left: 300px; top: 56px;
    color: var(--paper); font-size: 19px; font-weight: 400; letter-spacing: .03em;
  }
  .contact {
    position: absolute; left: 292px; color: var(--text-light);
    font-size: 11.5px; line-height: 1.35;
  }
  .contact-phone { top: 150px; }
  .contact-email { top: 206px; }
</style>
</head>
<body>
<main class="stage">

  <section class="card card-front" aria-label="Card front">
    <svg class="card-shapes" width="520" height="297" viewBox="0 0 520 297">
      <polygon class="front-band" fill="var(--teal)"
        points="0,240 250,240 260,230 270,240 520,240 520,297 0,297"/>
    </svg>
    <div class="brand">
      <span class="brand-dot"></span>
      <span class="brand-name">BRIGHTLANE COVERAGE</span>
    </div>
  </section>

  <section class="card card-back" aria-label="Card back">
    <svg class="card-shapes" width="520" height="297" viewBox="0 0 520 297">
      <rect class="dark-panel" x="240" y="0" width="280" height="297" fill="var(--charcoal)"/>
      <polygon class="name-band" fill="var(--teal)"
        points="240,42 520,42 520,98 240,98 240,78 226,70 240,62"/>
      <circle cx="274" cy="70" r="16" fill="var(--paper)"/>
      <circle cx="274" cy="65" r="5.5" fill="var(--teal)"/>
      <path d="M264 79 a10 8 0 0 1 20 0 z" fill="var(--teal)"/>
      <line x1="252" y1="138" x2="500" y2="138" stroke="var(--rule)" stroke-width="1"/>
      <line x1="252" y1="192" x2="500" y2="192" stroke="var(--rule)" stroke-width="1"/>
      <line x1="252" y1="234" x2="500" y2="234" stroke="var(--rule)" stroke-width="1"/>
      <circle cx="271" cy="165" r="10" fill="var(--teal)"/>
      <path d="M267 159 l3 0 l1 3 l-2 1.5 a8 8 0 0 0 3.5 3.5 l1.5 -2 l3 1 l0 3 a2 2 0 0 1 -2 1.5 a11 11 0 0 1 -10 -10 a2 2 0 0 1 2 -1.5 z"
        fill="var(--paper)"/>
      <circle cx="271" cy="213" r="10" fill="var(--teal)"/>
      <rect x="265" y="209" width="12" height="8" fill="var(--paper)"/>
      <polyline points="265,209 271,214 277,209" fill="none" stroke="var(--teal)" stroke-width="1"/>
    </svg>

    <div class="brand">
      <span class="brand-dot"></span>
      <span class="brand-name">BRIGHTLANE<br>COVERAGE</span>
    </div>

    <p class="holder-name">DALE HOSKIRK</p>
    <p class="contact contact-phone">Phone: 517.364.2908<br>Fax: 877.245.3196</p>
    <p class="contact contact-email">Dale.Hoskirk@brightlanecoverage.com</p>
  </section>

</main>
</body>
</html>
```